Southern Coastal Biofab Alliance Ecosystem

We recently published an article describing the Southern Coastal Biofab alliance ecosystem.
https://pagedrift.example/morrowlane-press/docs/bench_and_cell_review_jun_jul_2021/4

I would like to create a logo or graphic design to represent this initiative. We are thinking of having a graphic with a hand that holds the four sections ( Genetic Medicine, Industry, Research, University / Institutions) each represented by their own graphic in one complete picture. It will be used to represent the initiative on publications, document headers and letters. We need to keep it simple but also to clearly communicate the message.
Thanks.

Target Market(s)

Medicine, Industry, Research, University, Research Institutions and federal and local government

Requirements
Must have
• We need the graphic to represent the sections highlighted in the brief, we need some representation on research, industry/manufacturing and RNA. we need the Southern Coastal Biofab Alliance (SCBA) to be clearly represented that have deep expertise in the biology, chemistry, manufacture and use of RNA medicines.

```html
<!DOCTYPE html>
<html lang="en">
<head>
<meta charset="utf-8">
<title>Southern Coastal Biofab Alliance Ecosystem</title>
<link rel="stylesheet" href="https://fonts.googleapis.com/css2?family=Montserrat:wght@400;600&display=swap">
<style>
  :root {
    --page: #ffffff;
    --frame: #3a3a3a;
    --university-outer: #2c9a16;
    --university-inner: #5eba4c;
    --medicine-outer: #03255e;
    --medicine-inner: #203d72;
    --research-outer: #fdc300;
    --research-inner: #f4cb3b;
    --industry-outer: #ff5000;
    --industry-inner: #f1743a;
    --hub-light: #1b98d2;
    --hub-dark: #2a6fae;
    --ink-light: #ffffff;
  }
  html, body {
    margin: 0;
    padding: 0;
    width: 1200px;
    height: 1200px;
    overflow: hidden;
    background: var(--page);
  }
  .canvas {
    position: relative;
    width: 1200px;
    height: 1200px;
    box-sizing: border-box;
    border: 1.5px solid var(--frame);
    background: var(--page);
  }
  .ecosystem-wheel {
    display: block;
    width: 1200px;
    height: 1200px;
  }
  .sector-label {
    font-family: "Montserrat", sans-serif;
    font-weight: 400;
    font-size: 50px;
    fill: var(--ink-light);
  }
  .hub-title {
    font-family: "Montserrat", sans-serif;
    font-weight: 600;
    font-size: 32px;
    fill: var(--ink-light);
  }
  .sector-icon {
    fill: none;
    stroke: var(--ink-light);
    stroke-width: 4;
    stroke-linecap: round;
    stroke-linejoin: round;
  }
  .divider {
    stroke: var(--page);
    stroke-width: 6;
  }
</style>
</head>
<body>
<div class="canvas">
  <svg class="ecosystem-wheel" viewBox="0 0 1200 1200" xmlns="http://www.w3.org/2000/svg">
    <defs>
      <radialGradient id="hubGradient" cx="50%" cy="50%" r="50%">
        <stop offset="0%" stop-color="var(--hub-light)"/>
        <stop offset="100%" stop-color="var(--hub-dark)"/>
      </radialGradient>
      <filter id="wheelShadow" x="-10%" y="-10%" width="120%" height="120%">
        <feDropShadow dx="0" dy="2" stdDeviation="4" flood-color="#000" flood-opacity="0.12"/>
      </filter>
      <path id="arcUniversity" d="M252,600 A348,348 0 0 1 600,252"/>
      <path id="arcMedicine" d="M600,252 A348,348 0 0 1 948,600"/>
      <path id="arcResearch" d="M216,600 A384,384 0 0 0 600,984"/>
      <path id="arcIndustry" d="M600,984 A384,384 0 0 0 984,600"/>
    </defs>

    <!-- base disc -->
    <circle cx="600" cy="600" r="411" fill="var(--page)" filter="url(#wheelShadow)"/>

    <!-- outer ring sectors -->
    <path class="sector-outer university" d="M600,600 L196,600 A404,404 0 0 1 600,196 Z" fill="var(--university-outer)"/>
    <path class="sector-outer medicine" d="M600,600 L600,196 A404,404 0 0 1 1004,600 Z" fill="var(--medicine-outer)"/>
    <path class="sector-outer industry" d="M600,600 L1004,600 A404,404 0 0 1 600,1004 Z" fill="var(--industry-outer)"/>
    <path class="sector-outer research" d="M600,600 L600,1004 A404,404 0 0 1 196,600 Z" fill="var(--research-outer)"/>

    <!-- inner sectors -->
    <circle cx="600" cy="600" r="324" fill="var(--page)"/>
    <path class="sector-inner university" d="M600,600 L280,600 A320,320 0 0 1 600,280 Z" fill="var(--university-inner)"/>
    <path class="sector-inner medicine" d="M600,600 L600,280 A320,320 0 0 1 920,600 Z" fill="var(--medicine-inner)"/>
    <path class="sector-inner industry" d="M600,600 L920,600 A320,320 0 0 1 600,920 Z" fill="var(--industry-inner)"/>
    <path class="sector-inner research" d="M600,600 L600,920 A320,320 0 0 1 280,600 Z" fill="var(--research-inner)"/>

    <!-- quadrant dividers -->
    <line class="divider" x1="190" y1="600" x2="1010" y2="600"/>
    <line class="divider" x1="600" y1="190" x2="600" y2="1010"/>

    <!-- sector labels -->
    <text class="sector-label"><textPath href="#arcUniversity" startOffset="50%" text-anchor="middle">University</textPath></text>
    <text class="sector-label"><textPath href="#arcMedicine" startOffset="50%" text-anchor="middle">Genetic Medicine</textPath></text>
    <text class="sector-label"><textPath href="#arcResearch" startOffset="50%" text-anchor="middle">Research</textPath></text>
    <text class="sector-label"><textPath href="#arcIndustry" startOffset="50%" text-anchor="middle">Industry</textPath></text>

    <!-- sector icons -->
    <g class="sector-icon icon-graduation" transform="translate(369,372)">
      <polygon points="10,30 50,14 90,30 50,46"/>
      <path d="M26,37 v16 q24,10 48,0 v-16"/>
      <path d="M90,30 v22"/>
      <rect x="8" y="66" width="86" height="16" rx="8"/>
      <circle cx="50" cy="74" r="6"/>
      <path d="M46,80 v14 l4,-3 l4,3 v-14"/>
    </g>

    <g class="sector-icon icon-medical" transform="translate(729,369)">
      <path d="M35,5 h30 v30 h30 v30 h-30 v30 h-30 v-30 h-30 v-30 h30 z"/>
      <rect x="39" y="30" width="22" height="40" rx="11" transform="rotate(45 50 50)"/>
      <path d="M42,58 l16,-16"/>
    </g>

    <g class="sector-icon icon-microscope" transform="translate(372,736)">
      <path d="M40,8 l12,7 l-10,17 l-12,-7 z"/>
      <path d="M36,32 l-8,14"/>
      <path d="M50,40 a26,26 0 1 1 -20,44"/>
      <path d="M10,70 h30"/>
      <path d="M47,86 v8"/>
      <path d="M32,96 h30"/>
    </g>

    <g class="sector-icon icon-flask" transform="translate(726,723)">
      <path d="M36,8 h28"/>
      <path d="M42,8 v30 L18,84 q-4,10 8,10 h48 q12,0 8,-10 L58,38 v-30"/>
      <path d="M26,68 q12,-8 24,0 t24,0"/>
    </g>

    <!-- central hub -->
    <circle cx="600" cy="600" r="190" fill="url(#hubGradient)" stroke="var(--page)" stroke-width="6"/>
    <text class="hub-title" text-anchor="middle">
      <tspan x="600" y="550">Southern Coastal</tspan>
      <tspan x="600" y="590">Biofab</tspan>
      <tspan x="600" y="630">Alliance</tspan>
      <tspan x="600" y="670">(SCBA)</tspan>
    </text>
  </svg>
</div>
</body>
</html>
```